Financial Broker firm looking for Brochure design/Pdf-document

Job Type
Brochure Design/PDF-Document
Task Outline
Create a Brochure Design that also works for sending as pdf-document.
Task Description
We need a combined corporate brochure (Booklet style) to give out to potential clients as well as sending it to potential clients through Internet as pdf-document.
We need a background template with pictures and colors that gives the impression of professionalism, trustworthiness and seriousness. Attached text in English but the text will be translated into different languages to fit different markets. Therefore we would like to receive one template including the text and one without any text (but with the logo). Please inform us where (any) pictures and/or photos on the template have been taken from in order for us to buy and use them legally.
About Us
Our company Kelvora Trust AB is a financial brokerage company who provides a diversity of services for different selected partners (www.kelvoratrust.example).
Target Market
Companies on all levels, domestic or international
Requirements
Must Have:
-The text and logo attached below
Industry/Entity Type
Financial
Look and feel

```html
<!DOCTYPE html>
<html lang="en">
<head>
<meta charset="utf-8">
<title>Kelvora Trust AB – Brochure page</title>
<link rel="stylesheet" href="https://fonts.googleapis.com/css2?family=Arimo:wght@400;700&display=swap">
<style>
  :root {
    --page: #ffffff;
    --frame: #dcdddf;
    --panel: #ffffff;
    --ink: #1c1c1c;
    --blue-deep: #2f6fb0;
    --blue-light: #7fb6da;
    --photo-dark: #3b3c40;
    --photo-mid: #8e9096;
    --photo-light: #c9cacd;
    --chart-bg: #f4f4f4;
  }
  * { box-sizing: border-box; margin: 0; padding: 0; }
  html, body { width: 849px; height: 1200px; overflow: hidden; background: var(--page); }
  body { font-family: "Arimo", Arial, sans-serif; color: var(--ink); position: relative; }

  .frame { position: absolute; left: 38px; top: 0; width: 762px; height: 1167px; background: var(--frame); }
  .content-panel { position: absolute; left: 59px; top: 0; width: 599px; height: 945px; background: var(--panel); }

  .copy { position: absolute; left: 81px; top: 172px; width: 562px; font-size: 12.4px; line-height: 17.6px; }
  .copy p { text-align: justify; margin-bottom: 14px; }
  .copy h2 { font-size: 13px; font-weight: 700; margin-bottom: 2px; line-height: 18px; }
  .copy h3 { font-size: 12.6px; font-weight: 700; margin-bottom: 1px; }
  .benefits { list-style: none; width: 360px; margin-bottom: 16px; }
  .benefits li { padding-left: 12px; position: relative; }
  .benefits li::before { content: "•"; position: absolute; left: 0; }
  .closing { width: 350px; text-align: left !important; }

  .photo-cashflow {
    position: absolute; left: 495px; top: 580px; width: 283px; height: 208px;
    border: 5px solid #fff; background: linear-gradient(120deg, var(--photo-dark) 0%, var(--photo-mid) 55%, var(--photo-light) 100%);
  }

  .footer { position: absolute; left: 59px; top: 965px; width: 721px; height: 184px; background: #fff; }
  .contact-box {
    position: absolute; left: 10px; top: 10px; width: 232px; height: 168px;
    background: linear-gradient(135deg, var(--blue-deep) 0%, var(--blue-light) 100%);
    color: #fff; padding: 9px 14px; font-size: 11.6px; line-height: 15px;
  }
  .contact-box h4 { font-size: 11.8px; font-weight: 700; }
  .contact-box .spacer { height: 12px; }
  .growth-visual {
    position: absolute; left: 251px; top: 10px; width: 470px; height: 168px;
    background: linear-gradient(90deg, var(--chart-bg) 0%, #ffffff 60%, #e8e3de 100%);
  }
</style>
</head>
<body>
  <div class="frame"></div>
  <div class="content-panel"></div>

  <main class="copy">
    <p>The insurance is also applicable on attracting new clients, which gives your company the possibility to increase sales, open new markets and increase profits. Having a trade credit insurance is responsible business management, as it protects the cash flow and net profit of your company.</p>

    <h2>Bonding</h2>
    <p>Our insurance partners can issue bonds on behalf of its clients throughout the world, for almost all sec­tors of any industry and commerce. Your company has the advantage of being able to compete for a contract knowing that a bond will be available within the agreed underwriting criteria. Your credit line and working capital is thereby safeguarded.</p>

    <h2>Trade debt collection</h2>
    <p>Another benefit with our insurance partners is that they offer a trade debt collections service that corresponds to your company. They have experience in recognition of customers’ needs, not only to secure full payment as quickly as possible, but also to maintain a good relationship with clients.</p>

    <h2>Factoring</h2>
    <p>Factoring is a financial transaction whereby you as a company have the possibility to sell, or lend on, your account receivables (invoices) to a (pre)agreed rate. Compared to lending money where the focus is on your credit worthiness, factoring shifts the focus to your customers’ credit rating.</p>

    <h3>Your benefits with mortgage or selling your invoices are:</h3>
    <ul class="benefits">
      <li>Accelerated cash flow through faster collections</li>
      <li>Liquidity to boost working capital</li>
      <li>Increased sales in foreign markets by offering competitive terms of sale</li>
      <li>Opportunity to use supplier discounts</li>
      <li>Protection against credit losses (when selling your invoices to a factoring company)</li>
    </ul>
    <p class="closing">Depending on your need, demand, domestic or export, we will find a factoring company that will provide you with a solution that is right for your company.</p>
  </main>

  <div class="photo-cashflow" role="img" aria-label="Photo of a businessman holding a magnifying glass over the words cash flow"></div>

  <footer class="footer">
    <div class="contact-box">
      <h4>Contact Adress:</h4>
      <p>Kelvora Trust AB<br>Lindvägen 14<br>211 30 Malmö<br>Sweden<br>www.kelvoratrust.example</p>
      <div class="spacer"></div>
      <h4>Contacted by:</h4>
      <p>Elin Marsaud<br>Tel: +46 70 000 1234</p>
    </div>
    <div class="growth-visual" role="img" aria-label="Photo of a hand drawing a rising red growth line with an arrow"></div>
  </footer>
</body>
</html>
```